Recruitment technology firm needs a downloadable pdf to generate leads.

We need design work for a downloadable pdf that will serve as an educational document to visitors to our website. We help clients identify candidates that fit their job posting. We do that by defining the personality of the job and then assessing the personality of the candidates. We then mathematically compare and rank all the candidates against the job. Our colour scheme is blue. The final design should move from communicating a lack of fit or frustration to people fitting their job and success per the text we have built. People who download this lead generator will be added to our email list for re-marketing purposes. our website is www.brindlewaveadvisory.com. I've attached an example of a lead generator (ebike)for a business unrelated to ours.

Target Market(s)

Our target market is businesses of 50-300 people, we're targeting business owners or executives of entrepreneurial (vs. corporate) companies.

Colors
85acd3
3377b5
0455a3

Requirements
Must have
• Easy to read so text isn't overwhelming.
Nice to have
• Don't be compelled to use our website photos or those like it. I'd like this to reflect entrepreneurial companies, not corporate, suit and tie companies.

```html
<!DOCTYPE html>
<html lang="en">
<head>
<meta charset="utf-8">
<title>Hiring Mistakes – Points 3 to 5</title>
<link rel="stylesheet" href="https://fonts.googleapis.com/css2?family=Oswald:wght@700&family=Arimo:wght@400&display=swap">
<style>
  :root {
    --page-bg: #dedad9;
    --band: #066896;
    --band-fold: #155470;
    --heading-light: #45b8e8;
    --white: #ffffff;
    --orange-dark: #8e2a1c;
    --orange: #f47a22;
    --orange-light: #fdc60f;
    --navy: #14334c;
    --sky: #6ebde8;
    --tick: #0099cc;
    --swoosh-grey: #c9c6c8;
    --swoosh-blue: #1d6c9b;
  }
  * { margin: 0; padding: 0; box-sizing: border-box; }
  html, body { width: 848px; height: 1200px; overflow: hidden; }
  body {
    background: radial-gradient(ellipse at 50% 30%, #e4e1e0 0%, var(--page-bg) 70%, #d6d2d1 100%);
    position: relative;
    font-family: "Arimo", Arial, sans-serif;
  }
  .hero { position: absolute; left: 0; top: 0; width: 848px; height: 300px; }
  .tip-band { position: absolute; left: 0; width: 848px; }
  .tip-band svg { position: absolute; left: 0; top: 0; }
  .tip-content { position: relative; padding-left: 44px; padding-right: 44px; color: var(--white); }
  .tip-title {
    font-family: "Oswald", Impact, sans-serif;
    font-weight: 700;
    font-size: 29px;
    line-height: 1.1;
    letter-spacing: -0.3px;
    color: var(--white);
  }
  .tip-title.is-highlight { color: var(--heading-light); }
  .tip-body {
    display: flex;
    font-size: 22px;
    line-height: 26px;
    letter-spacing: -0.2px;
  }
  .tip-body .marker { width: 24px; flex: none; }
  .tip-one { top: 400px; height: 235px; }
  .tip-one .tip-content { padding-top: 2px; }
  .tip-two { top: 674px; height: 214px; }
  .tip-two .tip-content { padding-top: 2px; }
  .tip-two .tip-body { line-height: 29.5px; }
  .tip-three { top: 931px; height: 213px; }
  .tip-three .tip-content { padding-top: 18px; padding-left: 47px; }
  .tip-three .tip-body { padding-left: 22px; font-size: 22px; line-height: 25px; }
  .footer-swoosh { position: absolute; left: 0; top: 1150px; width: 848px; height: 50px; }
</style>
</head>
<body>

  <svg class="hero" viewBox="0 0 848 300" aria-hidden="false">
    <defs>
      <linearGradient id="ringWarm" x1="0" x2="1" y1="0" y2="0">
        <stop offset="0" stop-color="var(--orange-dark)"/>
        <stop offset="0.5" stop-color="var(--orange)"/>
        <stop offset="1" stop-color="var(--orange-light)"/>
      </linearGradient>
      <linearGradient id="ringCool" x1="0" x2="0" y1="0" y2="1">
        <stop offset="0" stop-color="var(--sky)"/>
        <stop offset="0.5" stop-color="#2a6d9c"/>
        <stop offset="1" stop-color="#0d1b2a"/>
      </linearGradient>
    </defs>
    <circle cx="174" cy="179" r="108" fill="url(#ringWarm)" role="img" aria-label="Candidate icon in an orange ring, not selected"/>
    <circle cx="427" cy="179" r="108" fill="url(#ringCool)" role="img" aria-label="Candidate icon in a blue ring, selected"/>
    <circle cx="668" cy="179" r="108" fill="url(#ringWarm)" role="img" aria-label="Candidate icon in an orange ring, not selected"/>
    <path class="tick" fill="var(--tick)"
      d="M334 102 L392 70 L424 126 Q470 45 540 0 L546 52 Q488 72 426 174 Z"/>
  </svg>

  <section class="tip-band tip-one">
    <svg width="848" height="235" viewBox="0 0 848 235">
      <rect x="0" y="0" width="807" height="235" fill="var(--band)"/>
      <polygon points="807,0 846,20 846,215 807,235" fill="var(--band-fold)"/>
    </svg>
    <div class="tip-content">
      <h2 class="tip-title">3.You assume knowledge and experience equals performance.</h2>
      <div class="tip-body">
        <span class="marker">a.</span>
        <p>Just because someone’s resume says they are a strong manager does not mean they are one. And yet this is how you screen and rank your candidates. The best resumes rise to the top. But resumes are a terrible predictor of performance. Success at one company does not mean success in yours. Who are you overlooking that may be a better performer?<br>(we have an idea below)</p>
      </div>
    </div>
  </section>

  <section class="tip-band tip-two">
    <svg width="848" height="214" viewBox="0 0 848 214">
      <rect x="0" y="0" width="807" height="214" fill="var(--band)"/>
      <polygon points="807,0 846,20 846,194 807,214" fill="var(--band-fold)"/>
    </svg>
    <div class="tip-content">
      <h2 class="tip-title is-highlight">4.You are biased and subjective in your assessment of others.</h2>
      <div class="tip-body">
        <span class="marker">a.</span>
        <p>You get attracted to certain resumes and backgrounds. You make judgement calls on phone interviews. You do the same when you meet someone and during an interview. Very few recruitment processes have a way of OBJECTIVELY ranking and comparing candidates. As a result we end up picking someone we like as opposed to someone who will excel in the job.</p>
      </div>
    </div>
  </section>

  <section class="tip-band tip-three">
    <svg width="848" height="213" viewBox="0 0 848 213">
      <rect x="0" y="0" width="807" height="213" fill="var(--band)"/>
      <polygon points="807,0 846,20 846,193 807,213" fill="var(--band-fold)"/>
    </svg>
    <div class="tip-content">
      <h2 class="tip-title">5. You think your “gut” makes good decisions.</h2>
      <div class="tip-body">
        <p>a. “Gut” has more to do with how likeable someone is than person’s ability to consistently behave in a manner that produces exceptional results. Do not make judgement calls on behaviours a candidate shows but may not be able to consistently repeat.</p>
      </div>
    </div>
  </section>

  <svg class="footer-swoosh" viewBox="0 0 848 50" preserveAspectRatio="none">
    <path d="M0 26 Q420 20 848 4 L848 50 L0 50 Z" fill="var(--swoosh-grey)"/>
    <path d="M0 34 Q430 38 848 10 L848 50 L0 50 Z" fill="var(--swoosh-blue)"/>
  </svg>

</body>
</html>
```